Business Card Design - Corporate

Create a sleek elegant business card layout while suggesting a color scheme. Convey cutting edge technology while maintaining a corporate feel that is easily readable.

Company designs and manufactures consumer electronic products for mass retail that are mainly app driven.

(vector logo and die-line provided)

Target Market(s)

Corporate level, tech industry.

Industry/Entity Type

Business

Contact Information for Business Card

Generic Info:

Name
Title
email
address
phone 1
phone 2
website (quelvane.com) on back

Font styles to use
Sans Serif

Requirements
Must have
• At least 2 colors + white on one side.
Nice to have
• Solid suggestion on color for logo and overall design. Color flood on back of card.
Should not have
• background texture like... marble, stone, patterns or circuit boards

```html
<!DOCTYPE html>
<html lang="en">
<head>
<meta charset="utf-8">
<title>Quelvane Business Card</title>
<link rel="stylesheet" href="https://fonts.googleapis.com/css2?family=Ubuntu:ital,wght@0,300;0,400;0,700;1,400&display=swap">
<style>
  :root {
    --stage: #e6e7e9;
    --card-white: #ffffff;
    --brand-blue: #1e7fcb;
    --brand-grey: #6a6b6d;
    --ink: #2b2b2d;
    --ink-soft: #4a4b4d;
    --shadow: rgba(0, 0, 0, 0.18);
  }
  * { box-sizing: border-box; margin: 0; padding: 0; }
  html, body {
    width: 1200px;
    height: 873px;
    overflow: hidden;
    background: var(--stage);
    font-family: "Ubuntu", sans-serif;
  }
  .sheet {
    position: relative;
    width: 1200px;
    height: 873px;
    display: flex;
    align-items: center;
    justify-content: center;
    gap: 60px;
  }
  .card {
    position: relative;
    width: 520px;
    height: 298px;
    overflow: hidden;
    border-radius: 3px;
    box-shadow: 0 10px 26px var(--shadow);
  }
  .card--front { background: var(--card-white); }
  .card--back { background: var(--brand-blue); }

  .wordmark {
    position: absolute;
    font-family: "Ubuntu", sans-serif;
    font-weight: 300;
    color: var(--brand-grey);
    letter-spacing: 0.18em;
    white-space: nowrap;
  }
  .card--front .wordmark {
    top: 30px;
    left: 34px;
    font-size: 40px;
  }
  .card--back .wordmark {
    top: 50%;
    left: 50%;
    transform: translate(-50%, -50%);
    font-size: 46px;
    color: var(--brand-grey);
  }

  .holder {
    position: absolute;
    top: 96px;
    left: 36px;
  }
  .holder__name {
    font-size: 19px;
    font-weight: 700;
    color: var(--ink);
  }
  .holder__title {
    margin-top: 3px;
    font-size: 10.5px;
    font-style: italic;
    color: var(--ink-soft);
  }

  .contact {
    position: absolute;
    top: 152px;
    left: 36px;
    list-style: none;
    font-size: 10.5px;
    line-height: 15px;
    color: var(--ink);
  }
  .contact__address { margin-bottom: 2px; }
  .contact__item {
    display: flex;
    align-items: center;
    gap: 6px;
  }
  .contact__icon { width: 10px; height: 10px; flex: none; }

  .accent-disc {
    position: absolute;
    border-radius: 50%;
    background: var(--brand-grey);
  }
  .card--front .accent-disc {
    width: 230px;
    height: 230px;
    right: -60px;
    bottom: -90px;
  }
  .card--back .accent-disc {
    width: 200px;
    height: 200px;
    left: -70px;
    top: -110px;
  }
</style>
</head>
<body>
<main class="sheet">
  <section class="card card--front" aria-label="Card front">
    <div class="wordmark">QUELVANE</div>
    <div class="holder">
      <p class="holder__name">Renata Solis</p>
      <p class="holder__title">Graphic Designer</p>
    </div>
    <ul class="contact">
      <li class="contact__address">Jl. Kenari 12 Blok C</li>
      <li class="contact__address">Tegalsari-Malang 65112</li>
      <li class="contact__address">Jawa Timur</li>
      <li class="contact__item">
        <svg class="contact__icon" viewBox="0 0 10 10" aria-hidden="true"><rect x="2.5" y="0.5" width="5" height="9" rx="1" fill="none" stroke="currentColor"/><rect x="4" y="7.5" width="2" height="0.8" fill="currentColor"/></svg>
        0812-4400-1180
      </li>
      <li class="contact__item">
        <svg class="contact__icon" viewBox="0 0 10 10" aria-hidden="true"><path d="M2 1.5 L4 1.5 L4.6 3.6 L3.6 4.4 Q4.4 6 5.8 6.6 L6.6 5.6 L8.6 6.2 L8.6 8.2 Q4.8 8.6 2.4 5.2 Q1.4 3.4 2 1.5 Z" fill="currentColor"/></svg>
        0812-4400-1181
      </li>
      <li class="contact__item">
        <svg class="contact__icon" viewBox="0 0 10 10" aria-hidden="true"><rect x="0.5" y="2" width="9" height="6" fill="none" stroke="currentColor"/><path d="M0.5 2 L5 5.5 L9.5 2" fill="none" stroke="currentColor"/></svg>
        renata.solis@quelvane.com
      </li>
      <li class="contact__item">
        <svg class="contact__icon" viewBox="0 0 10 10" aria-hidden="true"><circle cx="5" cy="5" r="4.4" fill="none" stroke="currentColor"/><ellipse cx="5" cy="5" rx="1.8" ry="4.4" fill="none" stroke="currentColor"/><line x1="0.6" y1="5" x2="9.4" y2="5" stroke="currentColor"/></svg>
        quelvane.com
      </li>
    </ul>
    <div class="accent-disc" aria-hidden="true"></div>
  </section>

  <section class="card card--back" aria-label="Card back">
    <div class="accent-disc" aria-hidden="true"></div>
    <div class="wordmark">QUELVANE</div>
  </section>
</main>
</body>
</html>
```